Business card for a "family office" company

Please provide professional looking business card designs, incorporating the attached logo and below details. Harrowmere Holdings Pty Ltd is a family office / financial investment company. We are looking for a modern, professional and contemporary card design.

Industry/Entity Type

Finance

Contact Information for Business Card

Name: Dean Mollick
Title: Director
Company: Harrowmere Holdings Pty Ltd
Email: harrowdean@quillnet.example
Mobile: 0462 735 418
Address: 4/312 Barnaby Parade, Wrenhaven WA 6199, Australia

Requirements
Must have
• All details above and the logo. logo only on back side. incorporate colours of logo
Nice to have
• up to you
Should not have
• ?

```html
<!DOCTYPE html>
<html lang="en">
<head>
<meta charset="utf-8">
<title>Harrowmere Holdings – Business Card</title>
<link rel="stylesheet" href="https://fonts.googleapis.com/css2?family=EB+Garamond:wght@400;600&display=swap">
<style>
  :root {
    --navy: #1e1d55;
    --navy-soft: #3f3d69;
    --paper: #ffffff;
    --backdrop: #ececec;
    --ink-light: #ffffff;
    --ink-dark: #1e1d55;
    --ink-body: #222222;
  }
  * { margin: 0; padding: 0; box-sizing: border-box; }
  html, body {
    width: 1200px; height: 586px; overflow: hidden;
    background: var(--backdrop);
    font-family: "EB Garamond", Georgia, serif;
  }
  .canvas { position: relative; width: 1200px; height: 586px; }

  .card {
    position: absolute; top: 129px;
    width: 502px; height: 301px; overflow: hidden;
  }

  /* Front */
  .card--front { left: 61px; background: var(--navy); }
  .front__emblem-area {
    position: absolute; left: 171px; top: 0; right: 0; bottom: 0;
    background: var(--navy-soft);
  }
  .front__identity { position: absolute; left: 34px; top: 198px; color: var(--ink-light); }
  .wordmark__name {
    font-variant: small-caps; font-size: 36px; line-height: 1;
    letter-spacing: 0.04em; font-weight: 400;
  }
  .wordmark__sub {
    font-size: 15px; letter-spacing: 0.42em; text-transform: uppercase;
    margin-top: 4px; font-weight: 400;
  }
  .front__web {
    font-size: 11px; letter-spacing: 0.22em; margin-top: 10px;
  }

  /* Back */
  .card--back { left: 619px; background: var(--paper); }
  .back__band {
    position: absolute; left: 0; right: 0; bottom: 0; height: 12px;
    background: var(--navy);
  }
  .back__wordmark {
    position: absolute; left: 0; right: 0; top: 102px;
    text-align: center; color: var(--ink-dark);
  }
  .back__wordmark .wordmark__name { font-size: 34px; }
  .back__wordmark .wordmark__sub { font-size: 13px; letter-spacing: 0.5em; margin-top: 2px; }

  .contact { position: absolute; left: 32px; top: 184px; }
  .contact__row {
    display: flex; align-items: center; gap: 10px;
    font-size: 13px; color: var(--ink-body); height: 26px;
  }
  .contact__icon { width: 18px; height: 18px; flex: none; }
  .contact__address {
    margin-top: 1px; font-size: 13.5px; font-weight: 600;
    color: var(--ink-dark); line-height: 1.35;
  }

  .person {
    position: absolute; right: 38px; top: 203px;
    text-align: right; color: var(--ink-dark);
  }
  .person__name { font-size: 19px; font-weight: 600; }
  .person__title { font-size: 13px; color: var(--ink-body); margin-top: 6px; }
</style>
</head>
<body>
<main class="canvas">

  <section class="card card--front" aria-label="Card front">
    <div class="front__emblem-area" role="img" aria-label="Large faint brand emblem decoration"></div>
    <div class="front__identity">
      <div class="wordmark__name">Harrowmere</div>
      <div class="wordmark__sub">Holdings</div>
      <div class="front__web">www.harrowmereholdings.example</div>
    </div>
  </section>

  <section class="card card--back" aria-label="Card back">
    <div class="back__wordmark">
      <div class="wordmark__name">Harrowmere</div>
      <div class="wordmark__sub">Holdings</div>
    </div>

    <div class="contact">
      <div class="contact__row">
        <svg class="contact__icon" viewBox="0 0 18 18" aria-hidden="true">
          <circle cx="9" cy="9" r="9" fill="var(--navy)"/>
          <path d="M5 6.5c0-1 .6-1.5 1.5-1.5h5c.9 0 1.5.5 1.5 1.5v.6h-2v-.8H7v.8H5z M5.5 8h7l.5 4.5H5z" fill="#fff"/>
          <circle cx="9" cy="10.3" r="1.2" fill="var(--navy)"/>
        </svg>
        <span>0462 735 418</span>
      </div>
      <div class="contact__row">
        <svg class="contact__icon" viewBox="0 0 18 18" aria-hidden="true">
          <circle cx="9" cy="9" r="9" fill="var(--navy)"/>
          <rect x="4.5" y="5.8" width="9" height="6.4" fill="#fff"/>
          <path d="M4.8 6.1 9 9.4l4.2-3.3" fill="none" stroke="var(--navy)" stroke-width="0.9"/>
        </svg>
        <span>harrowdean@quillnet.example</span>
      </div>
      <div class="contact__address">4/312 Barnaby Parade,<br>Wrenhaven WA 6199, Australia</div>
    </div>

    <div class="person">
      <div class="person__name">Dean Mollick</div>
      <div class="person__title">Director</div>
    </div>

    <div class="back__band"></div>
  </section>

</main>
</body>
</html>
```